KalVesta Website- Joomla Template

A website for a Plumber company. A one page design ( this is what i mean http://pallowdesign.example/en/#graph)
The website should be a template for Joomla, i will do the website in 3 languages
I want it to be elegant but not so that it looks like a consulting company.
My customers are private customers, my products are :
Main focus is on Fixing 24/7
then renovate bathrooms
replace heating systems
and Maintenance
I need 12 slides:
Who we are
News
Service
Maintenance
Renewable Energy
Sanitary
Heating
Ventilation
Partners
Useful Links
Contact us
of course a Facebook, twitter and G+ icon
try to make an innovative nice menu

```html
<!DOCTYPE html>
<html lang="en">
<head>
<meta charset="utf-8">
<title>KalVesta – Plumbing &amp; Heating</title>
<link rel="stylesheet" href="https://fonts.googleapis.com/css2?family=Raleway:wght@400;500;600&family=Open+Sans:wght@400;600;700&display=swap">
<style>
:root{
  --navy:#0d3d6b;
  --navy-deep:#0a3158;
  --navy-bar:#0b3660;
  --navy-card:#0f2f55;
  --green:#2f8d3b;
  --green-bright:#3da243;
  --white:#ffffff;
  --ink:#2b3440;
  --muted:#8e959c;
  --title-blue:#1d5c8e;
  --field:#0b2b4e;
  --footer:#0a2d52;
  --logo-grey:#eeeeee;
}
*{box-sizing:border-box;margin:0;padding:0}
html,body{width:1200px;height:4196px;overflow:hidden}
body{position:relative;font-family:"Open Sans",Arial,sans-serif;color:var(--ink);background:var(--white)}
.abs{position:absolute}
h2{font-family:"Raleway",Arial,sans-serif;font-weight:500;font-size:34px;text-align:center;position:absolute;left:0;width:1200px}

/* hero */
.hero{left:0;top:0;width:1200px;height:708px;background:linear-gradient(180deg,#eef1f4 0%,#e4e0da 35%,#d6d8dc 60%,#c9ccd3 100%)}
.hero-photo{position:absolute;inset:0;background:radial-gradient(ellipse at 50% 40%,rgba(255,255,255,.7),rgba(255,255,255,0) 60%),linear-gradient(180deg,rgba(200,170,140,0) 30%,rgba(150,120,100,.25) 80%)}
.emergency{left:140px;top:96px;display:flex;align-items:center;gap:14px;font-size:15px;color:#333}
.emergency .badge{width:40px;height:40px;border-radius:50%;border:3px solid #333}
.brand{left:0;width:1200px;top:100px;text-align:center;font-family:"Raleway",Arial,sans-serif;font-size:44px;font-weight:500;color:var(--navy);letter-spacing:1px}
.call{right:140px;top:100px;font-size:15px;color:#333;display:flex;align-items:center;gap:12px}
.hero-arrow{top:378px;width:30px;height:30px;border-radius:50%;border:2px solid rgba(255,255,255,.7)}
.scroll-down{left:582px;top:648px}

/* nav */
.nav{left:0;top:708px;width:1200px;height:56px;background:var(--navy-bar);display:flex;padding-left:140px}
.nav a{color:#fff;text-decoration:none;font-size:13px;line-height:56px;padding:0 13px}
.nav a.active{background:var(--green-bright);padding:0 22px}

/* features */
.features{left:0;top:764px;width:1200px;height:601px;background:var(--navy);color:#fff}
.features h2{top:64px;color:#fff}
.features .lead{top:128px;left:0;width:1200px;text-align:center;font-size:16px;letter-spacing:.3px}
.features .intro{top:156px;left:280px;width:640px;text-align:center;font-size:11.5px;line-height:16px;color:#d8e2ee}
.feature{top:243px;width:190px;height:293px;background:var(--navy-card);text-align:center}
.feature .icon{margin:36px auto 0;width:102px;height:102px}
.feature h3{font-family:"Raleway",Arial,sans-serif;font-weight:400;font-size:20px;line-height:22px;margin-top:22px;min-height:44px;display:flex;align-items:center;justify-content:center}
.feature p{font-size:10px;line-height:13px;padding:8px 20px 0;color:#dbe4ef}

/* who we are */
.about h2{top:1424px;color:var(--title-blue)}
.about p{left:180px;top:1488px;width:840px;text-align:center;font-size:13.5px;line-height:19px;color:var(--muted)}
.btn{background:var(--navy);color:#fff;font-size:13px;text-align:center}
.about .btn{left:540px;top:1586px;width:132px;height:30px;line-height:30px}

/* news */
.news-title{top:1694px;color:var(--title-blue)}
.news-card{top:1770px;width:438px;height:395px}
.news-card .photo{height:190px}
.news-card .tag{position:absolute;left:80px;top:176px;width:28px;height:28px;background:var(--green)}
.news-card .meta{position:absolute;left:0;top:210px;width:78px;text-align:right;font-size:10px;line-height:15px;color:#666}
.news-card h3{position:absolute;left:102px;top:214px;font-size:14px;font-weight:700;color:#222}
.news-card .text{position:absolute;left:102px;top:240px;width:320px;font-size:12px;line-height:18px;color:#666}
.news-card .read{position:absolute;left:102px;top:356px;width:80px;height:24px;line-height:22px;font-size:10px;font-weight:700;text-align:center;border:1px solid #333;color:#222}
.news-card .read.on{background:var(--navy);color:#fff;border-color:var(--navy)}

/* services */
.services{left:0;top:2288px;width:1200px;height:503px;background:var(--green);color:#fff}
.services h2{top:56px;color:#fff}
.services .lead{top:110px;left:0;width:1200px;text-align:center;font-size:16px}
.service{top:210px;width:220px;text-align:center}
.service svg{display:block;margin:0 auto}
.service span{display:block;margin-top:20px;font-size:20px}

/* gallery */
.tile{width:294px}
.tile .photo{height:154px}
.tile .label{text-align:center;font-size:18px;font-weight:600;color:#333;margin-top:14px}

/* links */
.links-title{top:3334px;color:var(--title-blue)}
.partner{top:3346px;width:132px;height:50px;background:var(--logo-grey)}
.partner-mark{top:3415px;width:100px;height:12px;background:#e2e2e2;border-radius:6px}
.dots{left:576px;top:3482px;display:flex;gap:9px}
.dots i{width:10px;height:10px;border-radius:50%;background:#222;display:block}

/* contact */
.contact{left:0;top:3566px;width:1200px;height:560px;background:linear-gradient(180deg,#0f4274 0%,#0c3a66 100%);color:#fff}
.contact h2{top:30px;color:#fff}
.contact .intro{left:150px;top:86px;width:900px;text-align:center;font-size:11px;line-height:16px;color:#dde6f0}
.contact h3{font-family:"Raleway",Arial,sans-serif;font-weight:500;font-size:26px;position:absolute}
.addr{left:140px;top:226px;font-size:12px;line-height:16px}
.addr strong{font-size:14px;display:block;margin-bottom:12px}
.addr dl{margin-top:30px;display:grid;grid-template-columns:60px auto;font-size:12px;line-height:16px}
.map{left:344px;top:232px;width:221px;height:188px;background:linear-gradient(135deg,#e9e6df,#d7d9d3)}
.field{background:var(--field);color:#ddd;font-size:12px;padding:6px 12px}
.send{left:727px;top:448px;width:218px;height:40px;line-height:40px;background:var(--green-bright);color:#fff;font-weight:700;font-size:18px;text-align:center}
.footer{left:0;top:4126px;width:1200px;height:70px;background:var(--footer);color:#dfe6ee;text-align:center;font-size:14px;line-height:70px}
</style>
</head>
<body>

<section class="hero abs">
  <div class="hero-photo" role="img" aria-label="Blurred photo of a bright interior room"></div>
  <div class="emergency abs"><span class="badge"></span>Fixing 24/7 for emergencies</div>
  <div class="brand abs">KalVesta</div>
  <div class="call abs">Call - 1800 - 555 - 0199
    <svg width="20" height="24" viewBox="0 0 20 24"><path d="M5 2c1.5-1 2.5 0 3.5 2l1 2.5c.5 1.3-.3 2-1.5 2.8.8 2.4 2.3 5 4.6 7.1 1.2-.8 2-1.4 3.2-.6l2 1.5c1.5 1 1.4 2.3.2 3.4C14 25 6 17 3 9 2 6 3 3.5 5 2z" fill="#333"/></svg>
  </div>
  <span class="hero-arrow abs" style="left:80px"></span>
  <span class="hero-arrow abs" style="right:80px"></span>
  <svg class="scroll-down abs" width="36" height="42" viewBox="0 0 36 42"><rect x="8" y="2" width="20" height="20" transform="rotate(45 18 12)" fill="none" stroke="#fff" stroke-width="2"/><path d="M11 24l7 7 7-7M11 32l7 7 7-7" fill="none" stroke="#fff" stroke-width="2"/></svg>
</section>

<nav class="nav abs">
  <a class="active">Home</a><a>Who we are</a><a>News</a><a>Service</a><a>Maintenance</a><a>Renewable Energy</a><a>Sanitary</a><a>Heating</a><a>Ventilation</a><a>Air Conditioning</a>
</nav>

<section class="features abs">
  <h2>Our Features</h2>
  <p class="lead abs">CRAS COMMODO MATTIS JUSTO NEC LOBORTIS. NAM UT TELLUS LOBORTIS, ULLAMCORPER MASSA SIT</p>
  <p class="intro abs">Cras suscipit porttitor porttitor. Morbi sit amet tincidunt sapien. Curabitur posuere lectus aliquet erat rutrum sollicitudin. In enim diam, ullamcorper quis libero et, ultricies commodo est. Quisque at ante vitae justo fermentum viverra ac eu justo. Ut luctus imperdiet lacus, eget laoreet erat posuere quis.</p>

  <div class="feature abs" style="left:140px">
    <svg class="icon" viewBox="0 0 102 102"><circle cx="51" cy="51" r="48" fill="#fff"/><circle cx="51" cy="51" r="38" fill="none" stroke="#0d3d6b" stroke-width="3"/><path d="M38 64l16-16m-4-8a8 8 0 1 0 12 10l-4-1-1-4 4-4a8 8 0 0 0-11-1zM36 66l3 3" stroke="#0d3d6b" stroke-width="5" stroke-linecap="round" fill="none"/></svg>
    <h3>Fixing 24/7</h3>
    <p>Praesent interdum blandit quam. Aenean in animi ab ante from dolor in reprehenderit in voluptate with esse cillum dolore.</p>
  </div>
  <div class="feature abs" style="left:386px">
    <svg class="icon" viewBox="0 0 102 102"><circle cx="51" cy="51" r="48" fill="#fff"/><circle cx="51" cy="51" r="38" fill="none" stroke="#0d3d6b" stroke-width="3"/><path d="M36 48a15 15 0 0 1 27-7M66 54a15 15 0 0 1-27 7" stroke="#0d3d6b" stroke-width="5" fill="none"/><path d="M60 34l5 8-9 1zM42 68l-5-8 9-1z" fill="#0d3d6b"/></svg>
    <h3>Renovate Bathrooms</h3>
    <p>Praesent interdum blandit quam. Aenean in animi ab ante from dolor in reprehenderit in voluptate with esse cillum dolore.</p>
  </div>
  <div class="feature abs" style="left:632px">
    <svg class="icon" viewBox="0 0 102 102"><circle cx="51" cy="51" r="48" fill="#fff"/><circle cx="51" cy="51" r="38" fill="none" stroke="#0d3d6b" stroke-width="3"/><circle cx="51" cy="49" r="14" fill="none" stroke="#0d3d6b" stroke-width="4"/><path d="M51 49l6-7M44 66h14" stroke="#0d3d6b" stroke-width="4" stroke-linecap="round"/></svg>
    <h3>Replace Heating Systems</h3>
    <p>Praesent interdum blandit quam. Aenean in animi ab ante from dolor in reprehenderit in voluptate with esse cillum dolore.</p>
  </div>
  <div class="feature abs" style="left:873px">
    <svg class="icon" viewBox="0 0 102 102"><circle cx="51" cy="51" r="48" fill="#fff"/><circle cx="51" cy="51" r="38" fill="none" stroke="#0d3d6b" stroke-width="3"/><circle cx="51" cy="51" r="15" fill="none" stroke="#0d3d6b" stroke-width="7" stroke-dasharray="10 4"/><circle cx="51" cy="51" r="5" fill="#0d3d6b"/></svg>
    <h3>Maintenance</h3>
    <p>Praesent interdum blandit quam. Aenean in animi ab ante from dolor in reprehenderit in voluptate with esse cillum dolore.</p>
  </div>
</section>

<section class="about">
  <h2>Who We Are</h2>
  <p class="abs">Sed ut perspiciatis unde omnis iste natus error sit voluptatem accusantium doloremque totam rem aperiam, eaque ipsa quae ab illo inventore veritatis et quasi architecto beat dicta sunt explicabo. Nemo enim ipsam voluptatem quia, sit amet turpis ut purus pellentesque ullamcorper sed ut nisl.</p>
  <div class="btn abs">Read More</div>
</section>

<section class="news">
  <h2 class="news-title">News</h2>
  <article class="news-card abs" style="left:140px">
    <div class="photo" role="img" aria-label="Photo of a chrome tap with splashing water" style="background:linear-gradient(135deg,#4f9ad6,#9fd0f0 50%,#2e6fb0)"></div>
    <span class="tag"></span>
    <div class="meta">21 Feb 14<br>John Doe<br>24 Comments</div>
    <h3>LOREM IPSUM DOILOR SIT</h3>
    <p class="text">Duis sed odio sit amet nibh vulputate cursus a sit amet mauris. Morbi accumsan ipsum velit. Nam nec tellus a odio tincidunt auctor a ornare odio. Sed non mauris vitae erat consequat auctor eu in elit.</p>
    <div class="read">READ ON</div>
  </article>
  <article class="news-card abs" style="left:621px">
    <div class="photo" role="img" aria-label="Photo of a radiator valve with copper pipes" style="background:linear-gradient(90deg,#f2f0ec,#e6e2dc 60%,#c98a5a 90%,#e9e5df)"></div>
    <span class="tag"></span>
    <div class="meta">21 Feb 14<br>John Doe<br>24 Comments</div>
    <h3>CONTANTRY POPILAR SIT AMIT LOREM</h3>
    <p class="text">Duis sed odio sit amet nibh vulputate cursus a sit amet mauris. Morbi accumsan ipsum velit. Nam nec tellus a odio tincidunt auctor a ornare odio. Sed non mauris vitae erat consequat auctor eu in elit.</p>
    <div class="read on">READ ON</div>
  </article>
</section>

<section class="services abs">
  <h2>Our Services</h2>
  <p class="lead abs">Lorem Ipsum has been the industry's standard dummy text ever since the 1500s</p>
  <div class="service abs" style="left:114px">
    <svg width="134" height="142" viewBox="0 0 134 142"><polygon points="67,3 129,37 129,105 67,139 5,105 5,37" fill="none" stroke="#fff" stroke-width="3"/><path d="M48 72l14 16 26-36" fill="none" stroke="#fff" stroke-width="5"/></svg>
    <span>Lorem Ipsum Sit</span>
  </div>
  <div class="service abs" style="left:366px">
    <svg width="134" height="142" viewBox="0 0 134 142"><polygon points="67,3 129,37 129,105 67,139 5,105 5,37" fill="none" stroke="#fff" stroke-width="3"/><path d="M48 72l14 16 26-36" fill="none" stroke="#fff" stroke-width="5"/></svg>
    <span>Contantry popilar</span>
  </div>
  <div class="service abs" style="left:623px">
    <svg width="134" height="142" viewBox="0 0 134 142"><polygon points="67,3 129,37 129,105 67,139 5,105 5,37" fill="none" stroke="#fff" stroke-width="3"/><path d="M48 72l14 16 26-36" fill="none" stroke="#fff" stroke-width="5"/></svg>
    <span>Lorem Ipsum Sit</span>
  </div>
  <div class="service abs" style="left:869px">
    <svg width="134" height="142" viewBox="0 0 134 142"><polygon points="67,3 129,37 129,105 67,139 5,105 5,37" fill="none" stroke="#fff" stroke-width="3"/><path d="M48 72l14 16 26-36" fill="none" stroke="#fff" stroke-width="5"/></svg>
    <span>Ipsum Sit</span>
  </div>
</section>

<section class="gallery">
  <div class="tile abs" style="left:140px;top:2853px"><div class="photo" role="img" aria-label="Photo of a plumber working on pipes" style="background:linear-gradient(135deg,#8a6a55,#c8b8a8 50%,#6c7680)"></div><div class="label">Maintance</div></div>
  <div class="tile abs" style="left:453px;top:2853px"><div class="photo" role="img" aria-label="Photo of wind turbines in a green field" style="background:linear-gradient(180deg,#dfe6ea,#c7d1d4 55%,#7f9b55)"></div><div class="label">Renewable Energy</div></div>
  <div class="tile abs" style="left:769px;top:2853px"><div class="photo" role="img" aria-label="Photo of a modern black washbasin and tap" style="background:linear-gradient(135deg,#f0f0f0,#bdbdbd 55%,#2a2a2a)"></div><div class="label">Sanitary</div></div>
  <div class="tile abs" style="left:140px;top:3068px"><div class="photo" role="img" aria-label="Photo of a thermometer against a hot city sunset" style="background:linear-gradient(180deg,#f6c14a,#e88a1f 60%,#5a3a1c)"></div><div class="label">Heating</div></div>
  <div class="tile abs" style="left:453px;top:3068px"><div class="photo" role="img" aria-label="Photo of a technician fitting ventilation ducts" style="background:linear-gradient(135deg,#dfe3e6,#a9b3ba 60%,#e8ecee)"></div><div class="label">Ventilation</div></div>
  <div class="tile abs" style="left:769px;top:3068px"><div class="photo" role="img" aria-label="Photo of a hand holding an air conditioner remote" style="background:linear-gradient(135deg,#e6eaee,#c2ccd4 60%,#9aa6b0)"></div><div class="label">Air Conditioning</div></div>
</section>

<section class="links">
  <h2 class="links-title">Useful Links</h2>
  <span class="partner abs" style="left:106px;top:3346px"></span>
  <span class="partner abs" style="left:278px"></span>
  <span class="partner abs" style="left:790px"></span>
  <span class="partner abs" style="left:962px"></span>
  <span class="partner-mark abs" style="left:122px"></span>
  <span class="partner-mark abs" style="left:296px"></span>
  <span class="partner-mark abs" style="left:462px"></span>
  <span class="partner-mark abs" style="left:636px"></span>
  <span class="partner-mark abs" style="left:806px"></span>
  <span class="partner-mark abs" style="left:980px"></span>
  <div class="dots abs"><i></i><i></i><i></i></div>
</section>

<section class="contact abs">
  <h2>Contact Us</h2>
  <p class="intro abs">Cras suscipit porttitor porttitor. Morbi sit amet tincidunt sapien. Curabitur posuere lectus aliquet erat rutrum sollicitudin. In enim diam, ullamcorper quis libero et, ultricies commodo est. Quisque at ante vitae justo fermentum viverra ac eu justo. Ut luctus imperdiet lacus, eget laoreet erat posuere quis.</p>
  <h3 style="left:140px;top:180px">Address</h3>
  <div class="addr abs">
    <strong>Lorem ipsum</strong>
    Harrowdene Rd<br>Ashbury AB12 3CD, UK
    <dl><dt>Phone:</dt><dd>+44 555 555 010</dd><dt>Fax:</dt><dd>+44 555 555 011</dd><dt>E-mail:</dt><dd>info@kalvesta.example</dd><dt>Skype:</dt><dd>KalVestaCall</dd></dl>
  </div>
  <div class="map abs" role="img" aria-label="Street map showing the office location"></div>
  <h3 style="left:604px;top:180px">Ask a question</h3>
  <div class="field abs" style="left:604px;top:238px;width:222px;height:28px">Name</div>
  <div class="field abs" style="left:838px;top:238px;width:225px;height:28px">E</div>
  <div class="field abs" style="left:604px;top:288px;width:459px;height:132px">Your question</div>
  <div class="send abs">SEND</div>
</section>

<footer class="footer abs">Yourwebsite.com © Copyright 2014, all rights reserved</footer>

</body>
</html>
```